TK Motorwerk braucht Werbeflyer
Zielgruppe
An Fahrzeugen:
-Leistungsteigerung
-Codier- und Nachrüstungen an ZRD und HOL Fahrzeugen
- KFZ Servicearbeiten Schwerpunkt ZRD
-Reifenhandel und Montage
- Autohandel
- Autoglaserbetrieb mit Zertifizierung und Versicherungsabwicklung
Aufgabenstellung
Größe soll DIN A5 sein.
Flyerdesign soll für die Vorder- und Rückseite erstellt werden.
Design bitte ähnlich wie Visitenkarte was ich hochgeladen habe
Die Vorderseite soll sich konzentieren auf:
Leistungsteigerung:
Es gibt bei uns zwei Alternativen
Softwareoptimierung und Tuningboxen
Softwareootimierung ab 299€
Tuningboxen ab 499€
Weitere Leistungen für die vorderseite :
Gaspedaltuning für direktere Gasannahme ab 149€
DPF abschaltung und Vmax aufhebung ab 199€
Rückseite soll sich auf den Rest konzentieren diese Wären:
- Codierarbeiten und Nachrüstarbeiten an ZRD und HOL Fahrzeugen
- Fehlerdiagnose, Steuergeräte einlernen und Softwareupdates an ZRD Fahrzeugen
- KFZ Servicearbeiten (Schwerpunkt ZRD)
- Reifenhandel und Montage
- Autoglas
- Autohandel Kauf und Verkauf im Kundenauftrag
An der Rückseite sollten kurze Texte geschrieben werden für die Leistungen
Für vorderseite bitte zwei Ausführungen einmal wie hier beschrieben und einmal mit dem Zusatz:
Nur bis zum 15. Dezember 10% Rabatt auf Softwareoptimierung und Tuningboxen bei Vorlage des Flyers

```html
<!DOCTYPE html>
<html lang="de">
<head>
<meta charset="utf-8">
<title>TK Motorwerk – Weitere Leistungen</title>
<link rel="stylesheet" href="https://fonts.googleapis.com/css2?family=Fjalla+One&display=swap">
<style>
  :root {
    --page-bg: #f4f4f4;
    --flyer-dark: #05080f;
    --flyer-navy: #0c1a33;
    --band-blue: #173c85;
    --band-blue-deep: #0d2558;
    --band-black: #000000;
    --band-red: #b0000f;
    --band-red-deep: #6d0008;
    --car-blue: #1e3f7a;
    --car-shadow: #0a1530;
    --text-white: #ffffff;
    --text-soft: #eef1f7;
  }
  html, body {
    margin: 0;
    padding: 0;
    width: 1200px;
    height: 1200px;
    overflow: hidden;
    background: var(--page-bg);
  }
  .flyer {
    position: absolute;
    left: 40px;
    top: 204px;
    width: 1120px;
    height: 792px;
    overflow: hidden;
    background: radial-gradient(ellipse at 35% 50%, var(--flyer-navy) 0%, var(--flyer-dark) 75%);
    font-family: "Fjalla One", "Arial Narrow", sans-serif;
    color: var(--text-white);
    box-shadow: 0 6px 24px rgba(0,0,0,0.25);
  }
  .car-photo {
    position: absolute;
    right: 0;
    top: 0;
    width: 420px;
    height: 100%;
    background:
      radial-gradient(ellipse at 85% 30%, rgba(150,20,30,0.55) 0%, rgba(150,20,30,0) 22%),
      radial-gradient(ellipse at 70% 50%, var(--car-blue) 0%, var(--car-shadow) 60%, rgba(5,8,15,0) 100%);
  }
  .band {
    position: absolute;
    left: 0;
    width: 100%;
  }
  .band--title {
    top: 62px; height: 58px;
    background: linear-gradient(90deg, rgba(176,0,15,0) 10%, var(--band-red-deep) 25%, var(--band-red) 50%, var(--band-red-deep) 75%, rgba(176,0,15,0) 90%);
  }
  .band--heading {
    height: 62px;
    background: linear-gradient(90deg, rgba(23,60,133,0) 5%, var(--band-blue-deep) 20%, var(--band-blue) 50%, var(--band-blue-deep) 80%, rgba(23,60,133,0) 95%);
  }
  .band--body {
    height: 84px;
    background: linear-gradient(90deg, rgba(0,0,0,0) 5%, rgba(0,0,0,0.85) 20%, var(--band-black) 50%, rgba(0,0,0,0.85) 80%, rgba(0,0,0,0) 95%);
  }
  .band--contact {
    top: 700px; height: 92px;
    background: linear-gradient(90deg, rgba(176,0,15,0) 12%, var(--band-red-deep) 28%, var(--band-red) 50%, var(--band-red-deep) 72%, rgba(176,0,15,0) 88%);
  }
  .flyer-title {
    position: absolute;
    top: 62px; left: 0; width: 100%;
    height: 58px; line-height: 58px;
    margin: 0;
    text-align: center;
    font-size: 36px;
    font-weight: 400;
    letter-spacing: 0.5px;
  }
  .services {
    position: absolute;
    top: 150px;
    left: 60px;
    width: 1000px;
    display: grid;
    grid-template-columns: 1fr 1fr;
    column-gap: 100px;
  }
  .service {
    height: 180px;
    text-align: center;
  }
  .service-title {
    margin: 0;
    height: 62px;
    display: flex;
    align-items: center;
    justify-content: center;
    font-size: 21px;
    line-height: 1.15;
    font-weight: 400;
  }
  .service-text {
    margin: 14px 0 0;
    font-size: 14px;
    line-height: 1.32;
    color: var(--text-soft);
  }
  .contact {
    position: absolute;
    top: 700px; left: 0; width: 100%; height: 92px;
    display: flex;
    flex-direction: column;
    justify-content: center;
    align-items: center;
    font-size: 23px;
    line-height: 1.2;
  }
  .contact-phone { font-size: 25px; }
</style>
</head>
<body>
  <section class="flyer">
    <div class="car-photo" role="img" aria-label="Heckansicht eines blauen Sportwagens mit roten Rückleuchten"></div>

    <div class="band band--title"></div>
    <div class="band band--heading" style="top:150px"></div>
    <div class="band band--body" style="top:222px"></div>
    <div class="band band--heading" style="top:330px"></div>
    <div class="band band--body" style="top:402px"></div>
    <div class="band band--heading" style="top:510px"></div>
    <div class="band band--body" style="top:582px"></div>
    <div class="band band--contact"></div>

    <h1 class="flyer-title">Weitere Leistungen</h1>

    <div class="services">
      <article class="service">
        <h2 class="service-title">Codier- und Nachrüstarbeiten<br>an ZRD und HOL-Fahrzeugen</h2>
        <p class="service-text">Lorem ipsum dolor sit amet, consetetur sadipscing elitr,<br>sed diam nonumy eirmod tempor invidunt ut labore et<br>dolore magna aliquyam erat, sed diam voluptua. At vero<br>eos et accusam et justo duo dolores et ea.</p>
      </article>
      <article class="service">
        <h2 class="service-title">Fehlerdiagnose, Einlernen der Steuergeräte<br>und Softwareupdates an ZRD-Fahrzeugen</h2>
        <p class="service-text">Lorem ipsum dolor sit amet, consetetur sadipscing elitr,<br>sed diam nonumy eirmod tempor invidunt ut labore et<br>dolore magna aliquyam erat, sed diam voluptua. At vero<br>eos et accusam et justo duo dolores et ea.</p>
      </article>
      <article class="service">
        <h2 class="service-title">KFZ-Servicearbeiten<br>(Schwerpunkt ZRD)</h2>
        <p class="service-text">Lorem ipsum dolor sit amet, consetetur sadipscing elitr,<br>sed diam nonumy eirmod tempor invidunt ut labore et<br>dolore magna aliquyam erat, sed diam voluptua. At vero<br>eos et accusam et justo duo dolores et ea.</p>
      </article>
      <article class="service">
        <h2 class="service-title">Reifenhandel<br>und Montage</h2>
        <p class="service-text">Lorem ipsum dolor sit amet, consetetur sadipscing elitr,<br>sed diam nonumy eirmod tempor invidunt ut labore et<br>dolore magna aliquyam erat, sed diam voluptua. At vero<br>eos et accusam et justo duo dolores et ea.</p>
      </article>
      <article class="service">
        <h2 class="service-title">Autoglasreparatur<br>und Austausch</h2>
        <p class="service-text">Lorem ipsum dolor sit amet, consetetur sadipscing elitr,<br>sed diam nonumy eirmod tempor invidunt ut labore et<br>dolore magna aliquyam erat, sed diam voluptua. At vero<br>eos et accusam et justo duo dolores et ea.</p>
      </article>
      <article class="service">
        <h2 class="service-title">Kauf und Verkauf von Fahrzeugen<br>im Kundenauftrag</h2>
        <p class="service-text">Lorem ipsum dolor sit amet, consetetur sadipscing elitr,<br>sed diam nonumy eirmod tempor invidunt ut labore et<br>dolore magna aliquyam erat, sed diam voluptua. At vero<br>eos et accusam et justo duo dolores et ea.</p>
      </article>
    </div>

    <address class="contact" style="font-style:normal">
      <span class="contact-web">tk-motorwerk.de</span>
      <span class="contact-street">Lindenweg 12,&nbsp; 56789 Talheim</span>
      <span class="contact-phone">0170 / 12 34 56 78</span>
    </address>
  </section>
</body>
</html>
```